Bright-loop stitchworks Business Card

embroidery printing

Target Market(s)

Businesses and public

Industry/Entity Type

Business

Contact Information for Business Card

Front of card..... Bright-loop stitchworks .... Dorian Felkway..... 868 512-7743.... Email... bright_loopstitchworks@mailvane.net

Back of card..... Bright-loop stitchworks embroidery & artwork

Colors
000000

```html
<!DOCTYPE html>
<html lang="en">
<head>
<meta charset="utf-8">
<title>Bright-loop stitchworks Business Card</title>
<link rel="stylesheet" href="https://fonts.googleapis.com/css2?family=Montserrat:wght@500;700&family=Cinzel:wght@400&display=swap">
<style>
  :root {
    --ink: #000000;
    --paper: #ffffff;
    --accent: #a3291f;
    --backdrop: #d9d9d9;
  }
  * { margin: 0; padding: 0; box-sizing: border-box; }
  html, body {
    width: 1200px; height: 900px; overflow: hidden;
    background: var(--backdrop);
  }
  .canvas {
    position: relative; width: 1200px; height: 900px;
  }
  .card {
    position: absolute; left: 300px; width: 600px; height: 343px;
    background: var(--ink); border-radius: 18px; overflow: hidden;
    color: var(--paper);
  }
  .card--back { top: 80px; }
  .card--front { top: 477px; }

  .brand-name {
    font-family: "Montserrat", sans-serif; font-weight: 700;
    color: var(--paper); text-transform: uppercase;
    line-height: 1.05; letter-spacing: 1px;
  }
  .card--back .brand-block {
    position: absolute; left: 0; right: 0; top: 125px; text-align: center;
  }
  .card--back .brand-name { font-size: 34px; }
  .tagline {
    margin-top: 14px;
    font-family: "Cinzel", serif; font-size: 17px; letter-spacing: 1.5px;
    color: var(--paper);
  }

  .accent-band { position: absolute; left: 0; top: 0; width: 600px; height: 343px; }
  .card--front .brand-name {
    position: absolute; left: 42px; top: 38px; font-size: 28px;
  }
  .holder-name {
    position: absolute; left: 42px; bottom: 30px;
    font-family: "Montserrat", sans-serif; font-weight: 700; font-size: 21px;
    letter-spacing: 0.5px; text-transform: uppercase;
  }
  .contact-list {
    position: absolute; left: 300px; top: 238px; list-style: none;
    font-family: "Montserrat", sans-serif; font-weight: 500; font-size: 13px;
  }
  .contact-item { display: flex; align-items: center; gap: 8px; margin-bottom: 8px; }
  .contact-icon { width: 12px; height: 12px; flex: none; }
</style>
</head>
<body>
<main class="canvas">
  <section class="card card--back">
    <div class="brand-block">
      <div class="brand-name">Bright-loop<br>stitchworks</div>
      <div class="tagline">EMBROIDERY &amp; ARTWORK</div>
    </div>
  </section>

  <section class="card card--front">
    <svg class="accent-band" viewBox="0 0 600 343" aria-hidden="true">
      <path d="M0 343 L0 250 C60 250 90 200 170 190 C260 180 300 140 380 125 C470 110 530 110 600 90 L600 343 Z"
            fill="var(--accent)" stroke="var(--paper)" stroke-width="3"/>
    </svg>
    <div class="brand-name">Bright-loop<br>stitchworks</div>
    <div class="holder-name">Dorian Felkway</div>
    <ul class="contact-list">
      <li class="contact-item">
        <svg class="contact-icon" viewBox="0 0 12 12" aria-hidden="true">
          <rect x="2.5" y="0.5" width="7" height="11" rx="1.5" fill="none" stroke="var(--paper)" stroke-width="1.2"/>
          <circle cx="6" cy="9.5" r="0.8" fill="var(--paper)"/>
        </svg>
        <span>868 512-7743</span>
      </li>
      <li class="contact-item">
        <svg class="contact-icon" viewBox="0 0 12 12" aria-hidden="true">
          <rect x="0.6" y="2" width="10.8" height="8" rx="1" fill="none" stroke="var(--paper)" stroke-width="1.2"/>
          <path d="M1 2.6 L6 6.6 L11 2.6" fill="none" stroke="var(--paper)" stroke-width="1.2"/>
        </svg>
        <span>bright_loopstitchworks@mailvane.net</span>
      </li>
    </ul>
  </section>
</main>
</body>
</html>
```